KL Taxidermy

I need business Cards with my logo and a background photo of one of my taxidermy mounts.
I would like a black back drop behind it all and what ever looks best for my contact information (red or white?)
Garrick Pembley
592-718-4409
kltaxidermy482@mailnook.example
Chatterloom page

```html
<!DOCTYPE html>
<html lang="en">
<head>
<meta charset="utf-8">
<title>KL Taxidermy – Business Card</title>
<link href="https://fonts.googleapis.com/css2?family=Saira+Condensed:wght@700&family=Saira:wght@500&display=swap" rel="stylesheet">
<style>
  :root {
    --stage: #1c1c1c;
    --card: #0b0b0b;
    --card-edge: #161616;
    --ink: #f2f2f2;
    --accent: #e3221f;
    --rule: #8a8a8a;
    --mount-light: #dedcd6;
    --mount-mid: #b3b0a8;
    --rock: #4a5058;
  }
  html, body {
    margin: 0;
    width: 1200px;
    height: 1200px;
    overflow: hidden;
    background: var(--stage);
  }
  .business-card {
    position: absolute;
    left: 50px;
    top: 285px;
    width: 1100px;
    height: 630px;
    border-radius: 22px;
    background: linear-gradient(160deg, var(--card-edge), var(--card) 55%);
    overflow: hidden;
  }
  .brand {
    position: absolute;
    left: 110px;
    top: 150px;
    display: flex;
    align-items: center;
    gap: 16px;
  }
  .brand-dot {
    width: 30px;
    height: 30px;
    border-radius: 50%;
    background: var(--ink);
  }
  .brand-name {
    font-family: "Saira", sans-serif;
    font-weight: 500;
    font-size: 44px;
    letter-spacing: 5px;
    text-transform: uppercase;
    color: var(--ink);
  }
  .mount-photo {
    position: absolute;
    left: 560px;
    top: 60px;
    width: 470px;
    height: 270px;
    border-radius: 18px;
    background: linear-gradient(180deg, var(--mount-light) 0%, var(--mount-mid) 72%, var(--rock) 100%);
  }
  .divider {
    position: absolute;
    left: 110px;
    top: 352px;
    width: 880px;
    height: 1px;
    background: var(--rule);
  }
  .owner-name {
    position: absolute;
    left: 110px;
    top: 368px;
    margin: 0;
    font-family: "Saira Condensed", sans-serif;
    font-weight: 700;
    font-size: 52px;
    line-height: 1.1;
    letter-spacing: 3px;
    text-transform: uppercase;
    color: var(--accent);
  }
  .contact-list {
    position: absolute;
    left: 580px;
    top: 385px;
    margin: 0;
    padding: 0;
    list-style: none;
    font-family: "Saira", sans-serif;
    font-weight: 500;
    font-size: 22px;
    letter-spacing: 0.5px;
    color: var(--ink);
  }
  .contact-item {
    display: flex;
    align-items: center;
    gap: 14px;
    height: 40px;
  }
  .contact-icon {
    width: 26px;
    height: 26px;
    flex: none;
  }
</style>
</head>
<body>
  <section class="business-card">
    <div class="mount-photo" role="img" aria-label="Photo of a white Dall sheep ram mount resting on a rock"></div>

    <div class="brand">
      <span class="brand-dot"></span>
      <span class="brand-name">KL Taxidermy</span>
    </div>

    <div class="divider"></div>
    <h1 class="owner-name">Garrick Pembley</h1>

    <ul class="contact-list">
      <li class="contact-item">
        <svg class="contact-icon" viewBox="0 0 28 28">
          <polygon points="14,1 25,7.5 25,20.5 14,27 3,20.5 3,7.5" fill="none" stroke="#e3221f" stroke-width="2.4"/>
          <path d="M9 9 l3 -1 l2 4 l-2 1.5 q1.5 3 4 4 l1.5 -2 l4 2 l-1 3 q-8 0 -11.5 -11.5z" fill="#e3221f"/>
        </svg>
        <span>592-718-4409</span>
      </li>
      <li class="contact-item">
        <svg class="contact-icon" viewBox="0 0 28 28">
          <polygon points="14,1 25,7.5 25,20.5 14,27 3,20.5 3,7.5" fill="none" stroke="#e3221f" stroke-width="2.4"/>
          <rect x="8" y="9.5" width="12" height="9" fill="#e3221f"/>
          <path d="M8 9.5 l6 5 l6 -5" fill="none" stroke="#0b0b0b" stroke-width="1.4"/>
        </svg>
        <span>kltaxidermy482@mailnook.example</span>
      </li>
      <li class="contact-item">
        <svg class="contact-icon" viewBox="0 0 28 28">
          <polygon points="14,1 25,7.5 25,20.5 14,27 3,20.5 3,7.5" fill="none" stroke="#e3221f" stroke-width="2.4"/>
          <circle cx="14" cy="14" r="4.5" fill="#e3221f"/>
        </svg>
        <span>kltaxidermy</span>
      </li>
    </ul>
  </section>
</body>
</html>
```